New Business Card Design Project

Use the flyer uploaded and website www.brightoakbuilders.com for inspiration.
List Our Services on Backside of business cards
Martin Hollis
Harborline Renovations Inc.
Licensed General Contractors
858-471-9063

Contact Information for Business Card

Use the flyer uploaded and website www.brightoakbuilders.com for inspiration. List Our Services on Backside of business cards Martin Hollis Harborline Renovations Inc. Licensed General Contractors 858-471-9063

```html
<!DOCTYPE html>
<html lang="en">
<head>
<meta charset="utf-8">
<title>Harborline Renovations – Business Card</title>
<link rel="stylesheet" href="https://fonts.googleapis.com/css2?family=Open+Sans:wght@400;600&family=Oswald:wght@400;700&family=Roboto:wght@700&display=swap">
<style>
  :root {
    --page: #f2f2f2;
    --ink: #111111;
    --brand-blue: #3182c8;
    --brand-red: #e41e26;
    --panel: rgba(255,255,255,0.94);
    --white: #ffffff;
  }
  html, body {
    margin: 0;
    width: 927px;
    height: 1200px;
    overflow: hidden;
    background: var(--page);
  }
  .card {
    position: absolute;
    left: 156px;
    width: 613px;
    height: 369px;
    filter: drop-shadow(3px 4px 3px rgba(0,0,0,0.35));
  }
  .card--front { top: 182px; }
  .card--back  { top: 647px; }
  .logo-name { font-family: "Open Sans", sans-serif; font-weight: 400; fill: var(--white); letter-spacing: 1px; }
  .holder-name { font-family: "Roboto", sans-serif; font-weight: 700; fill: var(--brand-red); }
  .tag-text { font-family: "Open Sans", sans-serif; font-weight: 400; fill: var(--white); }
  .phone { font-family: "Roboto", sans-serif; font-weight: 700; fill: var(--ink); letter-spacing: 1px; }
  .website { font-family: "Open Sans", sans-serif; font-weight: 400; fill: var(--ink); }
  .headline { font-family: "Oswald", sans-serif; font-weight: 700; fill: var(--brand-red); }
  .banner-text { font-family: "Oswald", sans-serif; font-weight: 700; fill: var(--white); letter-spacing: 4px; }
  .service { font-family: "Oswald", sans-serif; font-weight: 400; fill: var(--ink); }
  .tick { fill: none; stroke: var(--brand-red); stroke-width: 2.2; }
</style>
</head>
<body>

<svg class="card card--front" viewBox="0 0 843 507" xmlns="http://www.w3.org/2000/svg">
  <defs>
    <linearGradient id="livingRoom" x1="0" y1="0" x2="1" y2="1">
      <stop offset="0" stop-color="#e6ecef"/>
      <stop offset="0.5" stop-color="#cfd6da"/>
      <stop offset="1" stop-color="#a9b1b5"/>
    </linearGradient>
  </defs>
  <rect role="img" aria-label="Photo of a bright modern living room with a grey sofa and ocean-view windows" width="843" height="507" fill="url(#livingRoom)"/>
  <polygon points="0,0 843,0 843,92 0,271" fill="var(--ink)"/>
  <polyline points="44,441 44,236 707,89 707,229" fill="none" stroke="var(--brand-blue)" stroke-width="6"/>
  <line x1="707" y1="431" x2="707" y2="507" stroke="var(--brand-blue)" stroke-width="6"/>
  <polygon points="0,427 0,507 235,507" fill="var(--brand-blue)"/>

  <text class="logo-name" x="142" y="140" text-anchor="middle" font-size="19">HARBORLINE RENOVATIONS</text>

  <rect x="422" y="237" width="421" height="187" fill="var(--panel)"/>
  <text class="holder-name" x="451" y="298" font-size="36">MARTIN HOLLIS</text>
  <polygon points="452,308 806,308 790,337 452,337" fill="var(--brand-blue)"/>
  <text class="tag-text" x="461" y="331" font-size="23">Licensed General Contractors</text>
  <text class="phone" x="451" y="366" font-size="27">858-471-9063</text>
  <text class="website" x="451" y="395" font-size="23">www.brightoakbuilders.com</text>
</svg>

<svg class="card card--back" viewBox="0 0 843 507" xmlns="http://www.w3.org/2000/svg">
  <defs>
    <linearGradient id="kitchen" x1="0" y1="0" x2="0.6" y2="1">
      <stop offset="0" stop-color="#f0e6d6"/>
      <stop offset="0.55" stop-color="#dcc6a6"/>
      <stop offset="1" stop-color="#a8673a"/>
    </linearGradient>
  </defs>
  <rect role="img" aria-label="Photo of a warm kitchen with white cabinets, granite island and wood floor" width="843" height="507" fill="url(#kitchen)"/>
  <polygon points="0,0 349,0 48,440 0,440" fill="var(--ink)"/>
  <polygon points="0,423 0,507 235,507" fill="var(--brand-blue)"/>

  <text class="logo-name" x="125" y="121" text-anchor="middle" font-size="17">HARBORLINE RENOVATIONS</text>

  <rect x="451" y="8" width="392" height="487" fill="var(--panel)"/>
  <text class="headline" x="469" y="65" font-size="48" textLength="342" lengthAdjust="spacingAndGlyphs">OUR SERVICES ARE</text>
  <text class="headline" x="469" y="108" font-size="48" textLength="356" lengthAdjust="spacingAndGlyphs">100% GUARANTEED</text>
  <polygon points="470,122 826,122 812,163 470,163" fill="var(--brand-blue)"/>
  <text class="banner-text" x="494" y="154" font-size="30">SPECIALIZING IN:</text>

  <g class="services">
    <g transform="translate(480,196)"><circle class="tick" r="8.5"/><path class="tick" d="M-4,0 L-1,3.5 L6,-5"/></g>
    <text class="service" x="504" y="203" font-size="25">Remodel: Kitchen &amp; Bath</text>
    <g transform="translate(480,231)"><circle class="tick" r="8.5"/><path class="tick" d="M-4,0 L-1,3.5 L6,-5"/></g>
    <text class="service" x="504" y="238" font-size="25">Painting: Interior &amp; Exterior</text>
    <g transform="translate(480,265)"><circle class="tick" r="8.5"/><path class="tick" d="M-4,0 L-1,3.5 L6,-5"/></g>
    <text class="service" x="504" y="272" font-size="25">Flooring: Carpet, Vinyl, Wood</text>
    <g transform="translate(480,300)"><circle class="tick" r="8.5"/><path class="tick" d="M-4,0 L-1,3.5 L6,-5"/></g>
    <text class="service" x="504" y="307" font-size="25">Window &amp; Door Replacement</text>
    <g transform="translate(480,334)"><circle class="tick" r="8.5"/><path class="tick" d="M-4,0 L-1,3.5 L6,-5"/></g>
    <text class="service" x="504" y="341" font-size="25">Plumbing: Repairs &amp; Upgrades</text>
    <g transform="translate(480,369)"><circle class="tick" r="8.5"/><path class="tick" d="M-4,0 L-1,3.5 L6,-5"/></g>
    <text class="service" x="504" y="376" font-size="25">Energy-Efficient Upgrades</text>
    <g transform="translate(480,403)"><circle class="tick" r="8.5"/><path class="tick" d="M-4,0 L-1,3.5 L6,-5"/></g>
    <text class="service" x="504" y="410" font-size="25">Deck &amp; Patio Construction</text>
    <g transform="translate(480,438)"><circle class="tick" r="8.5"/><path class="tick" d="M-4,0 L-1,3.5 L6,-5"/></g>
    <text class="service" x="504" y="445" font-size="25">Water &amp; Mold Damage</text>
    <g transform="translate(480,473)"><circle class="tick" r="8.5"/><path class="tick" d="M-4,0 L-1,3.5 L6,-5"/></g>
    <text class="service" x="504" y="480" font-size="25">Garage Renovation</text>
  </g>
</svg>

</body>
</html>
```